"Maple Hollow" red wine label design

We are a Sydney based company. We need to design a wine label for a Australian red wine.
Front label include following info:
Our brand: "Maple Hollow";
Product name: "Shiraz 2016";
In the bottom with small font: "Wine of Australia", "750ml"
Back label:
the back label would need to be consistent with the front label, with space for one paragraph of tasting notes, and ingredient info etc.
we would like to use white, gold and blue in this label. It should make customer feel the magical and beautiful moment of starry night.

We also need a logo design for the wine brand: "Maple Hollow"

I have attached a few wine bottle that used blue to give you some inspirations.

We need the design in AI file format.

Target Market(s)

both men and women

Industry/Entity Type

It Company

Logo Text

Maple Hollow

Requirements
Nice to have
• gold borderline, words; use of blue and white

```html
<!DOCTYPE html>
<html lang="en">
<head>
<meta charset="utf-8">
<title>Maple Hollow Shiraz 2016 Label</title>
<link rel="stylesheet" href="https://fonts.googleapis.com/css2?family=Great+Vibes&family=Raleway:wght@400&display=swap">
<style>
  :root {
    --paper: #ffffff;
    --navy-deep: #020c2e;
    --navy-mid: #0b2a5a;
    --ink-blue: #0d2c74;
    --gold-light: #f3d66c;
    --gold: #d2aa3c;
    --gold-dark: #a87f22;
    --sky-top: #1c4fcf;
    --sky-mid: #1a74d0;
    --sky-low: #123b8e;
    --hills: #050a1c;
  }
  * { margin: 0; padding: 0; box-sizing: border-box; }
  html, body { width: 769px; height: 1200px; overflow: hidden; background: var(--paper); }
  .label {
    position: relative;
    width: 769px;
    height: 1200px;
    background: var(--paper);
    overflow: hidden;
  }
  .brand-name {
    position: absolute;
    top: 150px;
    left: 0;
    width: 100%;
    text-align: center;
    font-family: "Great Vibes", cursive;
    font-size: 70px;
    line-height: 1;
    color: var(--ink-blue);
  }
  .gold-rule {
    position: absolute;
    left: 0;
    top: 482px;
    width: 100%;
    height: 17px;
    background: linear-gradient(90deg, var(--gold-dark), var(--gold-light) 35%, var(--gold) 65%, var(--gold-dark));
  }
  .night-panel {
    position: absolute;
    left: 0;
    top: 499px;
    width: 100%;
    height: 629px;
    background: radial-gradient(ellipse at 50% 45%, var(--navy-mid) 0%, #06194a 50%, var(--navy-deep) 100%);
  }
  .feature-frame {
    position: absolute;
    left: 209px;
    top: 320px;
    width: 352px;
    height: 351px;
    background: var(--paper);
    border: 4px solid var(--gold);
    box-shadow: 0 4px 14px rgba(0, 0, 0, 0.35);
  }
  .feature-art {
    position: absolute;
    left: 9px;
    top: 9px;
    right: 9px;
    bottom: 9px;
    background:
      linear-gradient(180deg, transparent 68%, #0d2866 78%, var(--hills) 100%),
      radial-gradient(ellipse at 60% 35%, var(--sky-mid) 0%, var(--sky-top) 45%, var(--sky-low) 100%);
  }
  .product-name {
    position: absolute;
    top: 690px;
    left: 0;
    width: 100%;
    text-align: center;
    font-family: "Great Vibes", cursive;
    font-size: 108px;
    line-height: 1.2;
    color: var(--gold);
    background: linear-gradient(180deg, var(--gold-light), var(--gold) 55%, var(--gold-dark));
    -webkit-background-clip: text;
    background-clip: text;
    -webkit-text-fill-color: transparent;
  }
  .footer-band {
    position: absolute;
    left: 0;
    top: 1128px;
    width: 100%;
    height: 72px;
    background: linear-gradient(90deg, var(--gold-dark), var(--gold-light) 40%, var(--gold) 70%, var(--gold-dark));
    display: flex;
    align-items: center;
    justify-content: center;
    font-family: "Raleway", sans-serif;
    font-size: 27px;
    color: var(--ink-blue);
    gap: 16px;
  }
</style>
</head>
<body>
  <main class="label">
    <div class="brand-name">Maple Hollow</div>
    <div class="gold-rule"></div>
    <div class="night-panel"></div>
    <div class="feature-frame">
      <div class="feature-art" role="img" aria-label="Illustration of a starry blue night sky above dark rolling hills"></div>
    </div>
    <h1 class="product-name">Shiraz 2016</h1>
    <footer class="footer-band">
      <span class="origin">Wine of Australia</span>
      <span class="divider">|</span>
      <span class="volume">750ml</span>
    </footer>
  </main>
</body>
</html>
```